Marketing Brochure design required by Video Production company

We are looking for a slick, professional and eye-catching design for a marketing brochure that will showcase our company and its services.

Purpose:
The purpose of the brochure is to show our company as experienced, capable, professional and creative.

The Brochure:
The brochure will be 10 pages (including front and back cover), designed for printing in measurements of 16cm (height) x 18cm (wide).

Attached you will find:

1. Brochure Copy/Text - this is all the text to be included in the brochure. Text in red colour is not to be included in the design but is there as a guide to assist in the design

2. Design assets - our logo and hi-resolution images to be included in the design. The filenames of the images correspond with pages in the Brochure Copy/Text (as you will see)
* this does not seem to be attaching here in ArtMarketHub. Please download this file from stashbin here: https://www.stashbin.net/s/qk4tr7wnz2lpa0e/Product_Marketing_Brochure_Assets-2016-02-07.zip?dl=0

Design:
We would like the design to be open - not cramped or squashed in. Use of space is good. We want it to look very professional, but creative. And also feel simple and easy to read.

Colours to use - blues with black & white (black & white is our brand).

Please feel free to ask any questions you might have.

Thank you.

Industry/Entity Type

It Company

Font styles to use
Sans Serif

Colors
0592cd
3176b5
3276b5
33a6d7
85cae6
cee9f5
85acd3
eaf1f7

Requirements
Must have
• As per the description.
• Download design assets from:
• https://www.stashbin.net/s/qk4tr7wnz2lpa0e/Product_Marketing_Brochure_Assets-2016-02-07.zip?dl=0

```html
<!DOCTYPE html>
<html lang="en">
<head>
<meta charset="utf-8">
<title>Brochure Spread – Your Story &amp; Your Event</title>
<link href="https://fonts.googleapis.com/css2?family=Saira+Condensed:wght@700&family=Roboto+Condensed:wght@400&display=swap" rel="stylesheet">
<style>
  :root{
    --page-bg:#231f20;
    --canvas-bg:#e4e2e2;
    --blue:#0592cd;
    --orange:#f08a24;
    --white:#ffffff;
    --divider:#4a4647;
  }
  html,body{margin:0;padding:0;width:1200px;height:1200px;overflow:hidden;background:var(--canvas-bg);}
  .spread{
    position:absolute;left:0;top:336px;width:1456px;height:640px;
    transform:scale(0.8242);transform-origin:0 0;
    background:var(--page-bg);
    font-family:"Roboto Condensed",sans-serif;color:var(--white);
  }
  .page{position:absolute;top:0;height:640px;}
  .page--left{left:0;width:727px;border-right:1px solid var(--divider);}
  .page--right{left:728px;width:728px;}
  .photo{position:absolute;}
  .section-band{position:absolute;left:0;top:301px;width:166px;height:20px;background:var(--blue);}
  .page--right .section-band{width:168px;}
  .section-kicker,.section-title{
    position:absolute;margin:0;font-family:"Saira Condensed",sans-serif;font-weight:700;
    font-variant:small-caps;letter-spacing:.3px;line-height:1;white-space:nowrap;
  }
  .section-kicker{top:299px;font-size:25px;color:var(--white);}
  .section-title{top:322px;font-size:25px;color:var(--orange);}
  .column{position:absolute;top:361px;font-size:15.5px;line-height:17.3px;}
  .column p{margin:0 0 11px;}
  .column ul{margin:0 0 11px;padding:0;list-style:none;}
  .column li{position:relative;padding-left:21px;}
  .column li::before{content:"";position:absolute;left:2px;top:6px;width:6px;height:6px;border-radius:50%;background:var(--blue);}
  .column .tight{margin-bottom:0;}
</style>
</head>
<body>
<main class="spread">

  <section class="page page--left">
    <div class="photo" style="left:45px;top:43px;width:293px;height:119px;background:linear-gradient(90deg,#2a1e1a,#5a3a2c 60%,#3a2820);" role="img" aria-label="Man in blazer giving an interview in a wood-panelled room"></div>
    <div class="photo" style="left:45px;top:168px;width:293px;height:153px;background:linear-gradient(90deg,#e9eef1,#d8dde0 55%,#f2f2f0);" role="img" aria-label="Woman interviewed in front of a bright city window"></div>
    <div class="photo" style="left:344px;top:43px;width:194px;height:81px;background:linear-gradient(90deg,#8a6a52,#3b3644 60%,#24324a);" role="img" aria-label="Woman with glasses speaking on camera"></div>
    <div class="photo" style="left:344px;top:130px;width:194px;height:99px;background:linear-gradient(90deg,#9aa860,#c9a68a 55%,#e6ddd2);" role="img" aria-label="Woman interviewed in a produce store"></div>
    <div class="photo" style="left:344px;top:236px;width:194px;height:85px;background:linear-gradient(90deg,#2a2a2e,#4b4446 60%,#1e1c1e);" role="img" aria-label="Man interviewed in a dim room"></div>
    <div class="photo" style="left:545px;top:43px;width:134px;height:56px;background:linear-gradient(90deg,#c8d2da,#e8e2dc 60%,#b89a82);" role="img" aria-label="Young man in an office with a poster behind"></div>
    <div class="photo" style="left:545px;top:104px;width:134px;height:66px;background:linear-gradient(90deg,#5a4a3c,#7a6050 55%,#2e2724);" role="img" aria-label="Woman speaking in an interview"></div>
    <div class="photo" style="left:545px;top:177px;width:134px;height:82px;background:linear-gradient(90deg,#3a3028,#6a4e3c 55%,#2a2420);" role="img" aria-label="Man interviewed in a cafe"></div>
    <div class="photo" style="left:545px;top:266px;width:134px;height:55px;background:linear-gradient(90deg,#6a5a40,#a07a5c 55%,#4a3a2a);" role="img" aria-label="Bald bearded man in a workshop"></div>

    <div class="section-band"></div>
    <h2 class="section-kicker" style="left:59px;">Your Story</h2>
    <h3 class="section-title" style="left:59px;">Video Profile</h3>

    <div class="column" style="left:59px;width:300px;">
      <p>The Your STORY video profile is a combination of interviews and overlay footage designed to tell your business’ story.</p>
      <p class="tight">This style of video content helps your audience better understand:</p>
      <ul>
        <li>what makes you unique</li>
        <li>why they should trust you</li>
        <li>what your product offering is and how it works</li>
        <li>what your process is</li>
      </ul>
      <p>We’ll work with you to develop the best approach to deliver this in a sharp &amp; engaging fashion.</p>
    </div>

    <div class="column" style="left:368px;width:305px;">
      <p class="tight" style="margin-bottom:4px;">The package includes:</p>
      <ul>
        <li>Filming of interviews + overlay footage at your desired location</li>
        <li>A slick, professionally edited high definition video</li>
        <li>Quick turnaround time and review process</li>
        <li>An opportunity to make any changes before your video is finalised</li>
        <li>Delivery in your choice of formats</li>
      </ul>
      <p>Have additional requirements? No problem. Contact us to discuss a quote.</p>
    </div>
  </section>

  <section class="page page--right">
    <div class="photo" style="left:46px;top:43px;width:219px;height:278px;background:linear-gradient(90deg,#4a6a9a,#5a5a6a 50%,#1e1e26);" role="img" aria-label="Grey-haired speaker talking into a microphone"></div>
    <div class="photo" style="left:266px;top:43px;width:235px;height:278px;background:linear-gradient(180deg,#5a3a9a,#8a4ab0 55%,#c05a90);" role="img" aria-label="Guests dancing on a purple-lit stage"></div>
    <div class="photo" style="left:502px;top:43px;width:180px;height:278px;background:linear-gradient(180deg,#0e0c0e,#3a2a1e 55%,#6a3a24);" role="img" aria-label="Two women dancing at a night-time outdoor party"></div>

    <div class="section-band"></div>
    <h2 class="section-kicker" style="left:60px;">Your Event</h2>
    <h3 class="section-title" style="left:60px;">Event Coverage &amp; Highlights</h3>

    <div class="column" style="left:60px;width:300px;">
      <p style="margin-bottom:17px;">Got a launch, seminar, celebration, party or any other event that you want filmed? We’ve got you covered.</p>
      <p style="margin-bottom:17px;">The Your EVENT package provides creative event coverage, with the best parts of your event condensed into a slick highlights video that captures the vibe and essence of your event.</p>
      <p class="tight" style="margin-bottom:4px;">The package includes:</p>
      <ul>
        <li>Filming of your event exactly as you need</li>
      </ul>
    </div>

    <div class="column" style="left:372px;width:300px;line-height:19.2px;">
      <ul style="margin-bottom:18px;">
        <li>A slick, professionally edited high definition video, cut to music to suit your event</li>
        <li>An opportunity to review an edit and make changes before your video is finalised</li>
        <li>Delivery in your choice of formats</li>
        <li>Speech &amp; speaker recording also available</li>
      </ul>
      <p>Have additional requirements? No problem. Contact us to discuss a quote.</p>
    </div>
  </section>

</main>
</body>
</html>
```